Drag Show Flyer

We are holding a Drag Show, we are looking for something fun and exciting, over the top is a must.

Show Date: Saturday September 2nd 2017
Venue: Copper Kettle Cafe Bunbury
Doors open 7pm
Tickets: $50 per person, includes glass of sparkling on arrival and canapes
Tickets available at the Venue or from ticketlorna.com.au

Target Market(s)

Female, Hens Party, LBGT

Industry/Entity Type

Entertainment

Colors

Designer to choose colors to be used in the design.

Requirements
Must have
• Show Date: Saturday September 2nd 2017
• Venue: Copper Kettle Cafe Bunbury
• Doors open 7pm
• Tickets: $50 per person, includes glass of sparkling on arrival and canapes
• Tickets available at the Venue or from ticketlorna.com.au

```html
<!DOCTYPE html>
<html lang="en">
<head>
<meta charset="utf-8">
<title>Drag Show Flyer</title>
<link rel="stylesheet" href="https://fonts.googleapis.com/css2?family=Quicksand:wght@400;500;700&family=Kaushan+Script&display=swap">
<style>
  :root {
    --canvas-bg: #efefef;
    --magenta: #e3287f;
    --violet: #7b3f9f;
    --sky: #2f8fdb;
    --white: #ffffff;
    --ink: #33325a;
    --black-badge: #121212;
    --blush: #f6eef3;
  }
  html, body {
    margin: 0;
    padding: 0;
    width: 1200px;
    height: 1200px;
    overflow: hidden;
    background: var(--canvas-bg);
  }
  .flyer {
    position: absolute;
    left: 210px;
    top: 50px;
    width: 780px;
    height: 1100px;
    display: block;
  }
  .sans { font-family: "Quicksand", sans-serif; }
  .script { font-family: "Kaushan Script", cursive; }
  .date-small { font-size: 33px; font-weight: 500; fill: var(--white); }
  .date-big { font-size: 104px; font-weight: 700; fill: var(--white); }
  .year { font-size: 82px; font-weight: 700; fill: var(--white); }
  .venue-name { font-size: 35px; font-weight: 700; fill: var(--white); }
  .venue-town { font-size: 36px; font-weight: 500; fill: var(--white); }
  .title { font-size: 122px; fill: var(--white); }
  .doors { font-size: 42px; fill: var(--white); }
  .time { font-size: 86px; font-weight: 700; fill: var(--white); }
  .price { font-size: 74px; fill: var(--white); }
  .per-person { font-size: 34px; fill: var(--white); }
  .includes { font-size: 25px; font-weight: 500; fill: var(--ink); }
  .tickets { font-size: 21px; font-weight: 500; fill: var(--ink); }
  .tickets-site { font-weight: 700; }
  .badge-name-light { font-size: 17px; font-weight: 700; fill: var(--white); }
  .badge-name-dark { font-size: 16px; font-weight: 700; fill: var(--violet); }
  .badge-name-red { font-size: 16px; font-weight: 700; fill: var(--magenta); }
</style>
</head>
<body>
<svg class="flyer" viewBox="0 0 780 1100" xmlns="http://www.w3.org/2000/svg">
  <defs>
    <linearGradient id="wash-base" x1="0" y1="0" x2="1" y2="1">
      <stop offset="0" stop-color="#8c3aa0"/>
      <stop offset="0.45" stop-color="#8a55b5"/>
      <stop offset="1" stop-color="#3d86d6"/>
    </linearGradient>
    <radialGradient id="wash-pink" cx="0.5" cy="0.5" r="0.5">
      <stop offset="0" stop-color="#e0388c" stop-opacity="0.9"/>
      <stop offset="1" stop-color="#e0388c" stop-opacity="0"/>
    </radialGradient>
    <radialGradient id="wash-teal" cx="0.5" cy="0.5" r="0.5">
      <stop offset="0" stop-color="#3cc0d0" stop-opacity="0.85"/>
      <stop offset="1" stop-color="#3cc0d0" stop-opacity="0"/>
    </radialGradient>
    <linearGradient id="band-fill" x1="0" y1="0" x2="0" y2="1">
      <stop offset="0" stop-color="#e2358c"/>
      <stop offset="0.7" stop-color="#e0338a"/>
      <stop offset="1" stop-color="#c8338f"/>
    </linearGradient>
    <linearGradient id="arc-fill" x1="0" y1="0" x2="1" y2="0">
      <stop offset="0" stop-color="#3a7fd8"/>
      <stop offset="1" stop-color="#2f8fdb"/>
    </linearGradient>
    <filter id="pink-drop" x="-20%" y="-20%" width="140%" height="140%">
      <feDropShadow dx="3" dy="4" stdDeviation="0.5" flood-color="#e3287f"/>
    </filter>
    <filter id="blue-drop" x="-20%" y="-20%" width="140%" height="140%">
      <feDropShadow dx="2" dy="3" stdDeviation="0.5" flood-color="#2f8fdb"/>
    </filter>
    <filter id="soft-shadow" x="-20%" y="-20%" width="140%" height="140%">
      <feDropShadow dx="0" dy="3" stdDeviation="4" flood-color="#000" flood-opacity="0.35"/>
    </filter>
    <clipPath id="flyer-clip"><rect width="780" height="1100"/></clipPath>
  </defs>

  <g clip-path="url(#flyer-clip)">
    <g class="watercolour-wash" role="img" aria-label="Pink, violet and teal watercolour paint wash">
      <rect width="780" height="1100" fill="url(#wash-base)"/>
      <ellipse cx="420" cy="180" rx="260" ry="200" fill="url(#wash-pink)"/>
      <ellipse cx="700" cy="520" rx="200" ry="260" fill="url(#wash-teal)"/>
      <ellipse cx="60" cy="700" rx="160" ry="260" fill="url(#wash-teal)"/>
      <ellipse cx="640" cy="800" rx="200" ry="160" fill="url(#wash-pink)"/>
      <ellipse cx="330" cy="720" rx="220" ry="160" fill="url(#wash-pink)" opacity="0.6"/>
    </g>

    <rect class="date-band" x="35" y="0" width="188" height="1100" fill="url(#band-fill)" opacity="0.92"/>

    <circle class="venue-disc" cx="654" cy="31" r="190" fill="var(--sky)" stroke="var(--white)" stroke-width="3"/>

    <circle class="title-ring" cx="390" cy="545" r="270" fill="#ffffff" fill-opacity="0.08" stroke="var(--white)" stroke-width="5"/>

    <circle class="ticket-arc" cx="415" cy="1204" r="386" fill="url(#arc-fill)" stroke="var(--white)" stroke-width="4"/>

    <g class="show-date sans">
      <text class="date-small" x="44" y="66">Saturday</text>
      <text class="date-small" x="44" y="98">September</text>
      <text class="date-big" x="40" y="192">2nd</text>
      <text class="year" x="42" y="277">2017</text>
    </g>

    <g class="venue sans" text-anchor="middle">
      <text class="venue-name" x="618" y="67">Copper Kettle</text>
      <text class="venue-town" x="618" y="107">Cafe Bunbury</text>
    </g>

    <g class="venue-badge" filter="url(#soft-shadow)">
      <circle cx="659" cy="213" r="82" fill="var(--black-badge)" stroke="var(--white)" stroke-width="3"/>
    </g>
    <text class="badge-name-light sans" x="659" y="219" text-anchor="middle">Copper Kettle</text>

    <g class="show-title script" filter="url(#pink-drop)">
      <text class="title" x="160" y="540" transform="rotate(-12 160 540)">Drag</text>
      <text class="title" x="340" y="650" transform="rotate(-12 340 650)">Show</text>
    </g>

    <g class="doors-open">
      <g class="script" filter="url(#blue-drop)">
        <text class="doors" x="44" y="686" transform="rotate(-10 44 686)">Doors</text>
        <text class="doors" x="110" y="718" transform="rotate(-10 110 718)">open</text>
      </g>
      <text class="time sans" x="40" y="812">7pm</text>
    </g>

    <g class="partner-badges" filter="url(#soft-shadow)">
      <circle cx="654" cy="698" r="79" fill="var(--blush)" stroke="var(--white)" stroke-width="4"/>
      <circle cx="654" cy="877" r="79" fill="var(--white)" stroke="#e4e4e4" stroke-width="4"/>
    </g>
    <g class="partner-names sans" text-anchor="middle">
      <text class="badge-name-dark" x="654" y="704">the velvet group</text>
      <text class="badge-name-red" x="654" y="872">Loud Lip</text>
      <text class="badge-name-red" x="654" y="892">Productions</text>
    </g>

    <g class="price-block script" filter="url(#pink-drop)">
      <text class="price" x="302" y="918" transform="rotate(-8 302 918)">50$</text>
      <text class="per-person" x="300" y="966" transform="rotate(-10 300 966)">per person</text>
    </g>

    <g class="ticket-info sans" text-anchor="end">
      <text class="includes" x="744" y="1024">Includes glass of sparkling on arrival and canapes</text>
      <text class="tickets" x="744" y="1064">Tickets available at the Venue or from <tspan class="tickets-site">ticketlorna.com.au</tspan></text>
    </g>
  </g>
</svg>
</body>
</html>
```